Business Stationary
Business Cards and Letterheads
Professional
Dorian Hesketh
Principal/ Creative Director
12 Marrowfield Street
St. James
Trinidad and Tobago
plumvoraxialmarketing@brindlepost.com
I am now looking for Business Cards and stationary that reflect my company's intent to be distinctive....

```html
<!DOCTYPE html>
<html lang="en">
<head>
<meta charset="utf-8">
<title>PlumVorAxial Stationery</title>
<link href="https://fonts.googleapis.com/css2?family=Arimo:wght@400;700&display=swap" rel="stylesheet">
<style>
:root{
  --backdrop:#e6e3de;
  --paper:#ffffff;
  --navy:#1c2a74;
  --blue:#2f4db3;
  --sky:#8fa4dc;
  --flap:#8c8e93;
  --ink:#2c2f3a;
  --faint:#eceef3;
}
*{margin:0;padding:0;box-sizing:border-box}
html,body{width:1200px;height:497px;overflow:hidden;background:var(--backdrop);font-family:"Arimo",Arial,sans-serif;color:var(--ink)}
.stage{position:relative;width:1200px;height:497px}
.sheet{position:absolute;background:var(--paper);overflow:hidden;box-shadow:0 2px 6px rgba(0,0,0,.18)}
.swoosh{position:absolute;left:0;bottom:0;width:100%;height:100%}
.brand{display:flex;align-items:center;gap:4px;color:var(--navy);font-weight:700;white-space:nowrap}
.brand-dot{border-radius:50%;background:var(--navy);flex:none}
.tagline{font-size:4px;letter-spacing:.5px;color:var(--blue);text-transform:uppercase;white-space:nowrap}
.small{font-size:5px;line-height:1.45;white-space:nowrap}
.name{font-size:6.5px;font-weight:700;color:var(--navy)}
.role{font-size:4.5px;color:var(--ink)}
.watermark{position:absolute;color:var(--faint);font-weight:700;white-space:nowrap}

/* business cards */
.card{top:79px;width:161px;height:86px}
.card-front{left:19px}
.card-back{left:183px}
.card .person{position:absolute;left:8px;top:8px}
.card .brand{position:absolute;right:8px;top:8px;font-size:7px}
.card .brand-dot{width:7px;height:7px}
.card .contact{position:absolute;left:8px;top:44px}
.card .watermark{right:10px;top:40px;font-size:13px}

/* letterhead */
.letterhead{left:391px;top:29px;width:238px;height:372px}
.letterhead .brand{position:absolute;left:20px;top:16px;font-size:11px}
.letterhead .brand-dot{width:9px;height:9px}
.letterhead .tagline{position:absolute;left:33px;top:32px}
.letterhead .sender{position:absolute;right:12px;top:14px}
.letterhead .watermark{left:22px;top:120px;font-size:24px}

/* envelopes */
.envelope-back{left:648px;top:142px;width:300px;height:122px}
.envelope-back .brand{position:absolute;left:50%;top:18px;transform:translateX(-50%);font-size:9px}
.envelope-back .brand-dot{width:8px;height:8px}
.envelope-front{left:526px;top:233px;width:315px;height:223px}
.envelope-front .flap{position:absolute;left:0;top:0;width:100%;height:70px}
.envelope-front .brand{position:absolute;left:50%;top:40px;transform:translateX(-50%);font-size:9px;background:var(--paper);padding:2px 8px;border-radius:10px;border:1.5px solid var(--blue)}
.envelope-front .brand-dot{width:7px;height:7px}
.envelope-front .return{position:absolute;left:40px;top:145px;background:var(--paper);padding:2px 4px}
</style>
</head>
<body>
<main class="stage">

  <section class="sheet card card-front">
    <svg class="swoosh" viewBox="0 0 161 86" preserveAspectRatio="none" aria-hidden="true">
      <path d="M161 30 C120 60 80 78 40 86 L161 86 Z" fill="var(--sky)"/>
      <path d="M161 40 C125 66 95 80 70 86 L161 86 Z" fill="var(--blue)"/>
    </svg>
    <div class="person"><p class="name">Dorian Hesketh</p><p class="role">Principal/ Creative Director</p></div>
    <div class="brand"><span class="brand-dot"></span>PlumVorAxial</div>
    <div class="contact small"><p>12 Marrowfield Street</p><p>St. James, Trinidad</p><p>Tel: 868 555 0142</p><p>plumvoraxialmarketing@brindlepost.com</p></div>
  </section>

  <section class="sheet card card-back">
    <svg class="swoosh" viewBox="0 0 161 86" preserveAspectRatio="none" aria-hidden="true">
      <path d="M161 30 C120 60 80 78 40 86 L161 86 Z" fill="var(--sky)"/>
      <path d="M161 40 C125 66 95 80 70 86 L161 86 Z" fill="var(--blue)"/>
    </svg>
    <div class="person"><p class="name">Dorian Hesketh</p><p class="role">Principal/ Creative Director</p></div>
    <div class="brand"><span class="brand-dot"></span>PlumVorAxial</div>
    <div class="contact small"><p>12 Marrowfield Street</p><p>St. James, Trinidad</p><p>Tel: 868 555 0142</p><p>plumvoraxialmarketing@brindlepost.com</p></div>
    <p class="watermark">PlumVorAxial</p>
  </section>

  <section class="sheet letterhead">
    <svg class="swoosh" viewBox="0 0 238 372" preserveAspectRatio="none" aria-hidden="true">
      <path d="M238 300 C190 340 130 362 80 372 L238 372 Z" fill="var(--sky)"/>
      <path d="M238 318 C200 348 160 364 130 372 L238 372 Z" fill="var(--blue)"/>
    </svg>
    <div class="brand"><span class="brand-dot"></span>PlumVorAxial</div>
    <p class="tagline">Creative Marketing Solutions</p>
    <div class="sender small"><p>12 Marrowfield Street</p><p>St. James</p><p>Trinidad and Tobago</p><p>plumvoraxialmarketing@brindlepost.com</p></div>
    <p class="watermark">PlumVorAxial</p>
  </section>

  <section class="sheet envelope-back">
    <div class="brand"><span class="brand-dot"></span>PlumVorAxial</div>
  </section>

  <section class="sheet envelope-front">
    <svg class="flap" viewBox="0 0 315 70" preserveAspectRatio="none" aria-hidden="true">
      <path d="M0 0 L315 0 L315 10 L160 60 L0 10 Z" fill="var(--flap)"/>
    </svg>
    <svg class="swoosh" viewBox="0 0 315 223" preserveAspectRatio="none" aria-hidden="true">
      <path d="M0 90 C50 150 130 195 230 223 L0 223 Z" fill="var(--sky)"/>
      <path d="M0 110 C40 160 100 200 170 223 L0 223 Z" fill="var(--blue)"/>
    </svg>
    <div class="brand"><span class="brand-dot"></span>PlumVorAxial</div>
    <div class="return small"><p>12 Marrowfield Street</p><p>St. James</p><p>Trinidad and Tobago</p><p>plumvoraxialmarketing@brindlepost.com</p></div>
  </section>

</main>
</body>
</html>
```